New Company Business Card Design

I have a new company logo and I want a new business card design. I dont know if the logo file i attached is in the correct format or quality. We are a New York City Specialty construction Firm specializing in high risk out of the box projects. I want a simple and classy business card that people will his card is as crisp as the work his company does.

Target Market(s)

Clients in the heavy construction industry in New York City

Industry/Entity Type

Construction Company

Contact Information for Business Card

Simple Classy - DIFFERENT

Font styles to use
Other font styles liked:
• Mach the logo font in some way

Colors

Designer to choose colors to be used in the design.

Requirements
Must have
• Uniqueness
Nice to have
• Nothing particular - Just different and classy - Timeless
Should not have
• Goofy Shit or Gimmicky shit

```html
<!DOCTYPE html>
<html lang="en">
<head>
<meta charset="UTF-8">
<title>Halvern Associates – Business Card</title>
<link href="https://fonts.googleapis.com/css2?family=Lato:wght@300;400;700&display=swap" rel="stylesheet">
<style>
  :root{
    --page:#8e8e8c;
    --card:#dcdcd8;
    --ink:#1b1b1b;
    --muted:#6a6a6a;
    --brand:#1a72c4;
    --bar:#0d0d0d;
  }
  *{margin:0;padding:0;box-sizing:border-box}
  html,body{width:1200px;height:1200px;overflow:hidden}
  body{
    background:var(--page);
    font-family:'Lato',sans-serif;
    display:flex;flex-direction:column;align-items:center;justify-content:center;gap:70px;
  }
  .card{
    position:relative;width:880px;height:503px;background:var(--card);
    box-shadow:0 10px 30px rgba(0,0,0,.25);
  }
  /* front */
  .card--front .edge-bar{position:absolute;width:20px;height:120px;background:var(--bar)}
  .card--front .edge-bar--left{left:0;top:250px}
  .card--front .edge-bar--right{right:0;top:70px}
  .wordmark{
    position:absolute;left:0;right:0;top:50%;transform:translateY(-50%);
    display:flex;align-items:center;justify-content:center;gap:16px;
  }
  .wordmark__mark{width:30px;height:30px;background:var(--brand)}
  .wordmark__name{
    font-weight:700;color:var(--brand);font-size:50px;letter-spacing:1px;line-height:1.1;
  }
  /* back */
  .card--back .wordmark{right:auto;width:490px}
  .card--back .wordmark__name{font-size:30px}
  .card--back .wordmark__mark{width:20px;height:20px}
  .divider{position:absolute;left:490px;top:70px;width:1.5px;height:330px;background:#4a4a4a}
  .contact{position:absolute;left:535px;top:70px;right:30px;color:var(--ink)}
  .contact__name{font-size:34px;font-weight:400;line-height:1.1}
  .contact__title{font-size:19px;font-weight:300;color:var(--muted);margin-top:4px}
  .contact__list{list-style:none;margin-top:38px;display:flex;flex-direction:column;gap:12px}
  .contact__item{display:flex;align-items:center;gap:16px;font-size:15px;line-height:1.25}
  .contact__icon{width:30px;height:30px;flex:none}
</style>
</head>
<body>

  <section class="card card--front" aria-label="Card front">
    <span class="edge-bar edge-bar--left"></span>
    <span class="edge-bar edge-bar--right"></span>
    <div class="wordmark">
      <span class="wordmark__mark"></span>
      <span class="wordmark__name">Halvern Associates, Inc.</span>
    </div>
  </section>

  <section class="card card--back" aria-label="Card back">
    <div class="wordmark">
      <span class="wordmark__mark"></span>
      <span class="wordmark__name">Halvern Associates, Inc.</span>
    </div>
    <span class="divider"></span>
    <div class="contact">
      <h1 class="contact__name">Marcus T. Keller</h1>
      <p class="contact__title">Head of Marketing</p>
      <ul class="contact__list">
        <li class="contact__item">
          <svg class="contact__icon" viewBox="0 0 30 30"><circle cx="15" cy="15" r="15" fill="#111"/><rect x="11" y="7" width="8" height="16" rx="1.5" fill="none" stroke="#fff" stroke-width="1.5"/><circle cx="15" cy="20.5" r="0.9" fill="#fff"/></svg>
          <span>917-555-0148</span>
        </li>
        <li class="contact__item">
          <svg class="contact__icon" viewBox="0 0 30 30"><circle cx="15" cy="15" r="15" fill="#111"/><path d="M10 8.5l3 0 1.2 3.6-1.8 1.4a9 9 0 0 0 4.1 4.1l1.4-1.8 3.6 1.2 0 3a1.5 1.5 0 0 1-1.6 1.5A13 13 0 0 1 8.5 10.1 1.5 1.5 0 0 1 10 8.5z" fill="#fff"/></svg>
          <span>908-555-0172</span>
        </li>
        <li class="contact__item">
          <svg class="contact__icon" viewBox="0 0 30 30"><circle cx="15" cy="15" r="15" fill="#111"/><path d="M7 15l8-7 8 7h-2.5v7h-4v-4.5h-3V22h-4v-7z" fill="#fff"/></svg>
          <span>214 North Harbor Street<br>Linden, New Jersey 07036</span>
        </li>
        <li class="contact__item">
          <svg class="contact__icon" viewBox="0 0 30 30"><circle cx="15" cy="15" r="15" fill="#111"/><rect x="8" y="10" width="14" height="10" fill="#fff"/><path d="M8 10l7 6 7-6" fill="none" stroke="#111" stroke-width="1.3"/></svg>
          <span>marcus@halvern.com</span>
        </li>
        <li class="contact__item">
          <svg class="contact__icon" viewBox="0 0 30 30"><circle cx="15" cy="15" r="15" fill="#111"/><circle cx="15" cy="15" r="7" fill="none" stroke="#fff" stroke-width="1.5"/><ellipse cx="15" cy="15" rx="3" ry="7" fill="none" stroke="#fff" stroke-width="1.2"/><path d="M8 15h14" stroke="#fff" stroke-width="1.2"/></svg>
          <span>www.halvern.com</span>
        </li>
      </ul>
    </div>
  </section>

</body>
</html>
```